Postcard design to acquire new clients for my Property Management Company

I'm looking for a postcard design that I can send to prospective clients detailing information about my company and services.
Postcard should be eye catching and contain information from www.brightkeyrentals-example.com. I've provided a few screen shots for the most important information and my logo.
Target Market(s)
Real Estate
Industry/Entity Type
Real Estate
Font styles to use
Sans Serif
Requirements
Must have
- Must be eye catching!! this will be a direct mail piece - I'd like for the card to be read and not tossed in the trash immediately.
Design que from the logo.
A place to write / print the receipts name and address.
our physical address - 2287 Marble Lane, Lubbock, TX 79555.
Should not have
- the contact information on the business card is not accurate - please use info from website.

```html
<!DOCTYPE html>
<html lang="en">
<head>
<meta charset="utf-8">
<title>BrightKey Rentals Postcard</title>
<link href="https://fonts.googleapis.com/css2?family=Montserrat:wght@400;500;600;700;800&display=swap" rel="stylesheet">
<style>
  :root {
    --stage: #1a1a1a;
    --ink: #161616;
    --navy: #1d4f8a;
    --blue: #1b5a9c;
    --grey: #9d9d9d;
    --panel-grey: #9a9a9a;
    --light-grey: #bdbdbd;
    --white: #ffffff;
    --body-dark: #1e1e1e;
    --photo-sky: #3f6fc0;
    --photo-house: #e7ebef;
  }
  * { box-sizing: border-box; margin: 0; padding: 0; }
  html, body { width: 1200px; height: 564px; overflow: hidden; }
  body { background: var(--stage); font-family: "Montserrat", sans-serif; position: relative; }

  .card { position: absolute; top: 95px; overflow: hidden; box-shadow: 0 8px 22px rgba(0,0,0,.5); }
  .card-front { left: 30px; width: 560px; height: 373px; background: var(--ink); }
  .card-back { left: 610px; width: 561px; height: 370px; background: var(--white); }

  /* Front */
  .front-shapes { position: absolute; inset: 0; }
  .brand { position: absolute; left: 11px; top: 26px; display: flex; align-items: center; gap: 8px; }
  .brand-dot { width: 14px; height: 14px; background: var(--navy); }
  .brand-name { font-size: 22px; font-weight: 700; color: var(--navy); letter-spacing: 2px; }
  .headline { position: absolute; left: 5px; top: 133px; color: var(--white); line-height: 1; }
  .headline .line-1 { font-size: 47px; font-weight: 800; letter-spacing: -0.5px; }
  .headline .line-2 { font-size: 33px; font-weight: 600; margin-top: 8px; }
  .headline .line-3 { font-size: 27px; font-weight: 600; margin-top: 6px; padding-left: 2px; }
  .accent-rule { position: absolute; left: 0; top: 260px; width: 47px; height: 2px; background: var(--blue); }
  .tagline { position: absolute; left: 4px; top: 274px; font-size: 14px; line-height: 17px; color: var(--light-grey); font-weight: 500; }
  .contact-bar { position: absolute; left: 0; bottom: 0; width: 100%; height: 42px; display: flex; }
  .contact-label { width: 148px; background: var(--light-grey); color: var(--ink); font-weight: 700; font-size: 18px; display: flex; align-items: center; padding-left: 10px; }
  .contact-details { flex: 1; background: var(--navy); color: var(--white); display: flex; align-items: center; gap: 20px; padding-left: 20px; font-size: 13px; }
  .contact-item { display: flex; align-items: center; gap: 6px; white-space: nowrap; }

  /* Back */
  .services-panel { position: absolute; left: 0; top: 0; width: 334px; height: 100%; background: var(--panel-grey); }
  .services-title { position: absolute; left: 0; top: 9px; width: 100%; height: 23px; background: var(--ink); color: var(--white); font-weight: 800; font-size: 16px; text-align: center; line-height: 24px; letter-spacing: .3px; }
  .service { position: absolute; width: 140px; }
  .service-icon { position: absolute; left: -30px; top: 0; width: 22px; height: 22px; }
  .service h3 { font-size: 12px; font-weight: 600; color: var(--navy); line-height: 14px; white-space: nowrap; }
  .service p { font-size: 7.4px; line-height: 7.8px; color: var(--body-dark); margin-top: 3px; font-weight: 500; }
  .cta-band { position: absolute; left: 0; bottom: 0; width: 100%; height: 76px; background: var(--navy); color: var(--white); text-align: center; font-weight: 700; font-size: 16px; line-height: 20px; display: flex; flex-direction: column; justify-content: center; }
  .mail-panel { position: absolute; left: 334px; top: 0; right: 0; bottom: 0; }
  .stamp-box { position: absolute; left: 133px; top: 10px; width: 80px; height: 85px; border: 1.5px solid var(--ink); }
  .address-line { position: absolute; left: 20px; width: 193px; height: 1px; background: var(--ink); }
  .return-address { position: absolute; left: 20px; bottom: 16px; font-size: 7.5px; color: #555; font-weight: 500; }
</style>
</head>
<body>

<section class="card card-front">
  <svg class="front-shapes" width="560" height="373" viewBox="0 0 560 373">
    <polygon points="214,0 560,0 560,331 403,331" fill="var(--photo-sky)"/>
    <g role="img" aria-label="Photo of a white two-storey beach house with a pool">
      <defs>
        <linearGradient id="house-tone" x1="0" y1="0" x2="0" y2="1">
          <stop offset="0" stop-color="#4f7fcc"/>
          <stop offset=".3" stop-color="var(--photo-house)"/>
          <stop offset=".85" stop-color="#b9aa94"/>
          <stop offset="1" stop-color="#3f8fd0"/>
        </linearGradient>
      </defs>
      <polygon points="214,0 560,0 560,331 403,331" fill="url(#house-tone)"/>
    </g>
    <polygon points="0,0 214,0 240,48 205,90 0,90" fill="var(--white)"/>
    <line x1="240" y1="48" x2="403" y2="331" stroke="var(--white)" stroke-width="2"/>
  </svg>

  <div class="brand">
    <span class="brand-dot"></span>
    <span class="brand-name">BRIGHTKEY</span>
  </div>

  <div class="headline">
    <div class="line-1">PROPERTY</div>
    <div class="line-2">MANAGEMENT</div>
    <div class="line-3">ACROSS LUBBOCK</div>
  </div>
  <div class="accent-rule"></div>
  <p class="tagline">Maximize your financial returns with<br>support from our rental specialists</p>

  <div class="contact-bar">
    <div class="contact-label">Get In Touch</div>
    <div class="contact-details">
      <span class="contact-item">
        <svg width="15" height="15" viewBox="0 0 24 24"><path fill="#fff" d="M6.6 10.8a15.1 15.1 0 0 0 6.6 6.6l2.2-2.2a1 1 0 0 1 1-.25 11.4 11.4 0 0 0 3.6.57 1 1 0 0 1 1 1V20a1 1 0 0 1-1 1A17 17 0 0 1 3 4a1 1 0 0 1 1-1h3.5a1 1 0 0 1 1 1c0 1.25.2 2.45.57 3.57a1 1 0 0 1-.25 1z"/></svg>
        (806) 555-0147
      </span>
      <span class="contact-item">
        <svg width="17" height="12" viewBox="0 0 17 12"><rect x=".5" y=".5" width="16" height="11" fill="none" stroke="#fff"/><polyline points=".5,.5 8.5,7 16.5,.5" fill="none" stroke="#fff"/></svg>
        info@brightkeyrentals-example.com
      </span>
    </div>
  </div>
</section>

<section class="card card-back">
  <div class="services-panel">
    <div class="services-title">OUR SERVICES</div>

    <div class="service" style="left:38px; top:48px;">
      <svg class="service-icon" viewBox="0 0 24 24"><path fill="var(--navy)" d="M12 3 1 12h3v9h6v-6h4v6h6v-9h3z"/></svg>
      <h3>Property Marketing</h3>
      <p>Let us take over your marketing for you and we'll find a qualified renter quickly.</p>
    </div>
    <div class="service" style="left:38px; top:101px;">
      <svg class="service-icon" viewBox="0 0 24 24"><circle cx="8" cy="7" r="4" fill="var(--navy)"/><circle cx="17" cy="8" r="3" fill="var(--navy)"/><path fill="var(--navy)" d="M0 21c0-5 3-7 8-7s8 2 8 7zM14 14c4 0 9 1 9 6h-6c0-3-1-5-3-6z"/></svg>
      <h3>Tenant Screening</h3>
      <p>We don't just find someone to rent your home—we find the best renters. We screen all applications using fair housing guidelines to protect you.</p>
    </div>
    <div class="service" style="left:38px; top:160px;">
      <svg class="service-icon" viewBox="0 0 24 24"><text x="6" y="21" font-size="22" font-weight="700" fill="var(--navy)" font-family="Montserrat, sans-serif">$</text></svg>
      <h3>Rent Collection</h3>
      <p>Stop guessing when you'll receive your rental earnings every month and say hello to consistent payments. We keep your tenants current.</p>
    </div>
    <div class="service" style="left:38px; top:222px;">
      <svg class="service-icon" viewBox="0 0 24 24"><path fill="var(--navy)" d="M13 3h6l3 3-3 3-3-1-12 13-2-2L14 7z"/></svg>
      <h3>Maintenance</h3>
      <p>Still scrambling to respond to repair requests every time you receive a tenant call? Let us coordinate repair work on your behalf!</p>
    </div>

    <div class="service" style="left:193px; top:46px;">
      <svg class="service-icon" viewBox="0 0 24 24"><circle cx="10" cy="10" r="7" fill="none" stroke="var(--navy)" stroke-width="3"/><line x1="15" y1="15" x2="22" y2="22" stroke="var(--navy)" stroke-width="3.5"/></svg>
      <h3>Property Inspections</h3>
      <p>We visit every home in our portfolio regularly.</p>
    </div>
    <div class="service" style="left:193px; top:91px;">
      <svg class="service-icon" viewBox="0 0 24 24"><path fill="none" stroke="var(--navy)" stroke-width="2" d="M2 3v18h20"/><rect x="6" y="12" width="2" height="7" fill="var(--navy)"/><rect x="10" y="8" width="2" height="11" fill="var(--navy)"/><rect x="14" y="11" width="2" height="8" fill="var(--navy)"/><rect x="18" y="6" width="2" height="13" fill="var(--navy)"/></svg>
      <h3>Financial Reporting</h3>
      <p>Keep a handle on your real estate performance. We generate monthly statements so you can review income &amp; expenses at a moment's notice.</p>
    </div>
    <div class="service" style="left:193px; top:155px;">
      <svg class="service-icon" viewBox="0 0 24 24"><path fill="var(--navy)" d="M12 1 3 5v6c0 6 4 10 9 12 5-2 9-6 9-12V5z"/><path fill="#c9d6e6" d="M12 4v16c3.5-1.6 6-4.6 6-9V7z"/></svg>
      <h3>Evictions</h3>
      <p>When things go wrong inside your rental home, rest easy with the experts on your side. We will handle evictions for you &amp; find new renters when its over.</p>
    </div>
    <div class="service" style="left:193px; top:220px;">
      <svg class="service-icon" viewBox="0 0 24 24"><path fill="none" stroke="var(--navy)" stroke-width="2" d="M12 3v17M4 6h16M1 14l3-8 3 8zM17 14l3-8 3 8zM7 21h10"/></svg>
      <h3>Legal Guidance</h3>
      <p>Don't accidentally violate one of the many ordinances and housing laws governing your relationship with your tenants. Let us keep you compliant.</p>
    </div>

    <div class="cta-band">
      <span>CHOOSE THE RIGHT</span>
      <span>PROPERTY MANAGEMENT SYSTEM</span>
    </div>
  </div>

  <div class="mail-panel">
    <div class="stamp-box"></div>
    <div class="address-line" style="top:136px;"></div>
    <div class="address-line" style="top:191px;"></div>
    <div class="address-line" style="top:246px;"></div>
  </div>
</section>

</body>
</html>
```